LVM IT Solutions Provider

Please read attached documentation completely before beginning Project. Thank you!

Mark Forge Project Requirements

Thank you for your interest in this design contest. We are always welcome to questions and are looking forward to seeing what you can come up with.

The logo is located on the current site homepage http://www.lumavex.com/

Bootstrap

We work on a Bootstrap platform with our custom built CMS. We require all designs to be

sized accordingly with the bootstrap grid system found here: http://getframelyn.com/css/#grid

Start of Competition Requirements

At the start of a competition, we are looking for general Home Page Design concepts and interior page design concepts as well.

HOME PAGE DESIGN

Any changes requested by the client in the original designs

Responsive Tablet View (using standard bootstrap media queries, we need to see an

example of a tablet size home page view)

Responsive Phone View (using standard bootstrap media queries, we need to see an

example of a phone size home page view)

INTERIOR PAGE DESIGN

These pages are general content pages. Our CMS allows for the creation of unlimited

pages and gives the client control of adding them. Interior Page Designs can be built

with 1 column, 2 columns (either right side bar or left sidebar)

Examples of buttons and button states,

Examples of drop down menus

Examples of H1 through H5 plus body copy

We uploaded a clean logo to use on the project. Thank you.

We added a updated Creative Brief document to help out. Please take a look thanks!

```html
<!DOCTYPE html>
<html lang="en">
<head>
<meta charset="utf-8">
<title>LVM – IT Solutions Provider</title>
<link rel="stylesheet" href="https://fonts.googleapis.com/css2?family=Lato:wght@300;400;700;900&family=Open+Sans:ital,wght@0,400;0,600;1,400&display=swap">
<style>
:root{
  --blue:#0d4f9c;
  --blue-dark:#0a3f80;
  --gold:#e8a90c;
  --ink:#1c1c1c;
  --text:#555a60;
  --muted:#8a8f95;
  --line:#e4e7ea;
  --tab:#eceef0;
  --soft:#f3f5f7;
  --footer:#2e3034;
  --footer-line:#3c3f44;
  --footer-text:#a9adb2;
  --bottom:#232528;
  --white:#ffffff;
}
*{box-sizing:border-box;margin:0;padding:0}
html,body{width:1200px;height:3072px;overflow:hidden}
body{position:relative;background:var(--white);font-family:"Open Sans",Arial,sans-serif;color:var(--text);font-size:13px;line-height:1.85}
h1,h2,h3,h4,.nav,.btn,.tab{font-family:"Lato",Helvetica,sans-serif}
.abs{position:absolute}
.btn{display:inline-block;background:var(--blue);color:var(--white);font-weight:700;font-size:15px;letter-spacing:.5px;text-transform:uppercase;padding:0 24px;line-height:48px;border-radius:2px}
.btn-sm{font-size:13px;font-weight:400;text-transform:none;line-height:32px;padding:0 16px;letter-spacing:0}
.btn-ghost{background:var(--white);color:var(--ink);border:2px solid var(--ink);line-height:44px}

/* header */
.site-header{left:0;top:0;width:1200px;height:139px;background:var(--white)}
.brand{left:112px;top:26px;display:flex;align-items:center;gap:14px}
.brand-mark{width:22px;height:22px;border-radius:50%;background:var(--gold)}
.brand-name{font-family:"Lato",sans-serif;font-weight:900;font-size:64px;line-height:1;color:var(--blue);letter-spacing:1px}
.top-contact{right:110px;top:14px;display:flex;gap:34px;font-size:12px;color:var(--text)}
.top-contact span{display:flex;align-items:center;gap:9px}
.nav{right:110px;top:70px;display:flex;gap:50px;font-size:14px;color:#5b6066;text-transform:uppercase;letter-spacing:.3px}
.nav .active{color:var(--gold)}

/* hero */
.hero{left:0;top:139px;width:1200px;height:506px;background:linear-gradient(120deg,#0b2f55 0%,#2a6aa6 35%,#6fa8d6 55%,#21507f 80%,#0c2a4a 100%)}
.hero-panel{left:651px;top:76px;width:434px;height:352px;background:rgba(255,255,255,.9);padding:26px 28px}
.hero-panel h1{font-weight:400;font-size:30px;line-height:1.38;color:var(--ink)}
.hero-panel h1 b{font-weight:700;color:var(--blue)}
.hero-panel h1 .gold{color:var(--gold);font-weight:700}
.hero-panel h1 .dark{color:var(--ink);font-weight:900}
.hero-panel p{margin-top:26px;font-size:13px;line-height:1.85;color:var(--text)}
.hero-actions{margin-top:30px;display:flex;gap:16px}

/* welcome */
.tabs{left:110px;top:702px;width:255px}
.tab{height:65px;line-height:65px;padding-left:28px;font-size:21px;color:#6b7076;background:var(--tab);border-bottom:2px solid #d6dade}
.tab.active{background:linear-gradient(#1a62b5,var(--blue-dark));color:var(--white);border:0}
.welcome{left:407px;top:694px;width:682px}
.welcome h2{font-size:29px;font-weight:400;color:var(--ink);letter-spacing:.5px}
.welcome p{margin-top:24px;font-size:12.5px;line-height:1.95}
.shadow-rule{left:0;top:962px;width:1200px;height:12px;background:radial-gradient(ellipse at top,rgba(0,0,0,.08),rgba(0,0,0,0) 70%)}

/* services */
.services{left:82px;top:974px;width:1040px;display:grid;grid-template-columns:repeat(3,1fr)}
.service{height:340px;padding:66px 30px 0 30px;border-right:1px solid var(--line);border-bottom:1px solid var(--line);display:grid;grid-template-columns:74px 1fr;align-content:start}
.service:nth-child(3n){border-right:0}
.service:nth-child(n+4){border-bottom:0}
.service svg{width:46px;height:46px}
.service h3{font-size:21px;font-weight:400;line-height:1.4;color:var(--ink)}
.service p{grid-column:2;margin-top:26px;font-size:12.5px;line-height:1.9;color:var(--muted);max-width:205px}
.service .btn{grid-column:2;justify-self:start;margin-top:26px}

/* mission */
.mission{left:110px;top:1795px;width:480px}
.mission h2,.hiring h2{font-size:29px;font-weight:400;color:var(--ink)}
.mission p,.hiring p{margin-top:26px;font-size:13px;line-height:1.9}
.mission .btn,.hiring .btn{margin-top:34px}
.mission-photo{left:625px;top:1736px;width:450px;height:394px;background:linear-gradient(160deg,#d9dde2,#8aa2bf 55%,#4c6486)}

.hiring-band{left:0;top:2130px;width:1200px;height:365px;background:var(--soft)}
.hiring-photo{left:110px;top:2150px;width:515px;height:345px;background:linear-gradient(180deg,#c9ccd1,#52565d 55%,#22252a)}
.hiring{left:653px;top:2196px;width:440px}

/* partners */
.partners{left:110px;top:2530px;width:980px;height:70px;display:flex;justify-content:space-between;align-items:center}
.partner{width:100px;height:40px;border-radius:20px;background:#d3d6da}
.partner.round{width:46px;height:46px;border-radius:50%;background:#3a3c40}
.partners-rule{left:0;top:2628px;width:1200px;height:14px;background:#e9ebed}

/* footer */
.footer{left:0;top:2642px;width:1200px;height:368px;background:var(--footer);color:var(--footer-text)}
.fcol{position:absolute;top:40px}
.fcol h4{font-size:12.5px;font-weight:700;color:var(--white);text-transform:uppercase;letter-spacing:.5px;margin-bottom:22px}
.about{left:131px;width:200px;font-style:italic;font-size:12px;line-height:1.82;color:#878b90}
.posts{left:373px;width:225px}
.posts li{list-style:none;font-size:11.5px;line-height:1.4;padding:0 0 11px;margin-bottom:11px;border-bottom:1px solid var(--footer-line);color:#c9ccd0;white-space:nowrap}
.tweets{left:612px;width:210px;font-size:12px;line-height:1.8}
.tweets p{margin-bottom:22px}
.tweets b{color:#c9ccd0;font-weight:400}
.tweets i{color:#8e9297}
.contact{left:893px;width:200px;font-size:12px;line-height:1.85}
.contact .row{display:flex;gap:12px;align-items:center;margin-top:8px}
.bottom-bar{left:0;top:3010px;width:1200px;height:62px;background:var(--bottom);color:#8a8e93;font-size:11px}
.copy{left:131px;top:22px}
.social{right:136px;top:16px;display:flex;gap:16px}
.social span{width:22px;height:22px;border-radius:50%;border:1.5px solid #6d7176}
.tip{left:886px;top:-18px;background:#3a3d42;color:#d6d9dc;font-size:10px;padding:2px 8px}
</style>
</head>
<body>

<header class="site-header abs">
  <div class="brand abs"><span class="brand-mark"></span><span class="brand-name">LVM</span></div>
  <div class="top-contact abs">
    <span><svg width="12" height="12" viewBox="0 0 24 24"><path fill="#555a60" d="M6.6 10.8a15 15 0 0 0 6.6 6.6l2.2-2.2c.3-.3.7-.4 1-.2 1.1.4 2.3.6 3.6.6.6 0 1 .4 1 1V20c0 .6-.4 1-1 1A17 17 0 0 1 3 4c0-.6.4-1 1-1h3.5c.6 0 1 .4 1 1 0 1.3.2 2.5.6 3.6.1.3 0 .7-.2 1z"/></svg>(555) 214-0387</span>
    <span><svg width="13" height="10" viewBox="0 0 26 20"><rect width="26" height="20" rx="2" fill="#555a60"/><path d="M2 3l11 8 11-8" stroke="#fff" stroke-width="2" fill="none"/></svg>info@lumavex.com</span>
  </div>
  <nav class="nav abs">
    <span class="active">Home</span><span>About Us</span><span>Division</span><span>Products &amp; Services</span><span>Contact Us</span>
  </nav>
</header>

<section class="hero abs" role="img" aria-label="Woman touching a glowing digital interface with world map and scanning graphics">
  <div class="hero-panel abs">
    <h1>Technology <b>SOLUTIONS</b> For National <span class="gold">SECURITY</span> And Global <span class="dark">DEFENCE</span></h1>
    <p>Lorem ipsum dolor sit amet, consectetuer adipiscing elit, sed diam nonummy nibh euismod tincidunt ut laoreet dolore magna aliquam erat volutpat.</p>
    <div class="hero-actions"><span class="btn">Get Started</span><span class="btn btn-ghost">Learn More</span></div>
  </div>
</section>

<div class="tabs abs">
  <div class="tab active">Welcome</div>
  <div class="tab">About Us</div>
  <div class="tab">Our Key Features</div>
</div>
<section class="welcome abs">
  <h2>WELCOME TO LVM</h2>
  <p>Lorem ipsum dolor sit amet, consectetuer adipiscing elit, sed diam nonummy nibh euismod tincidunt ut laoreet dolore magna aliquam erat volutpat. Ut wisi enim ad minim veniam, quis nostrud exerci tation ullamcorper suscipit lobortis nisl ut aliquip ex ea commodo consequat. Duis autem vel eum iriure dolor in hendrerit in vulputate velit esse molestie consequat, vel illum dolore eu feugiat nulla facilisis<br>&nbsp;consequat. Duis autem vel eum iriure dolor in hendrerit in vulputate velit esse molestie consequat, vel illum dolore eu feugiat nulla facilisis</p>
</section>
<div class="shadow-rule abs"></div>

<section class="services abs">
  <article class="service">
    <svg viewBox="0 0 48 48" fill="none" stroke="#0d4f9c" stroke-width="3"><circle cx="10" cy="12" r="5"/><circle cx="38" cy="22" r="5"/><circle cx="16" cy="38" r="5"/><path d="M14 15l20 6M35 26L20 35M11 17l3 16"/></svg>
    <h3>Communicationa &amp;<br>Networking</h3>
    <p>Lorem ipsum dolor sit amet, consectetuer adipiscing elit, sed diam nonummy nibh euismod tincidunt ut laoreet dolore magna</p>
    <span class="btn btn-sm">Read More</span>
  </article>
  <article class="service">
    <svg viewBox="0 0 48 48" fill="none" stroke="#0d4f9c" stroke-width="3"><rect x="8" y="10" width="32" height="24" fill="#0d4f9c"/><path d="M2 4v8M2 4h8M46 4v8M46 4h-8M2 44v-8M2 44h8M46 44v-8M46 44h-8"/></svg>
    <h3>Technology<br>Insertion</h3>
    <p>Lorem ipsum dolor sit amet, consectetuer adipiscing elit, sed diam nonummy nibh euismod tincidunt ut laoreet dolore magna</p>
    <span class="btn btn-sm">Read More</span>
  </article>
  <article class="service">
    <svg viewBox="0 0 48 48" fill="none" stroke="#0d4f9c" stroke-width="3"><path d="M4 4v40h42"/><path d="M8 36c6-28 14-28 18-6s12 4 16-8"/><circle cx="18" cy="18" r="3"/><circle cx="34" cy="30" r="3"/></svg>
    <h3>Simulation And<br>Test</h3>
    <p>Lorem ipsum dolor sit amet, consectetuer adipiscing elit, sed diam nonummy nibh euismod tincidunt ut laoreet dolore magna</p>
    <span class="btn btn-sm">Read More</span>
  </article>
  <article class="service">
    <svg viewBox="0 0 48 48" fill="none" stroke="#0d4f9c" stroke-width="3"><path d="M24 3l18 7v12c0 12-8 20-18 23C14 42 6 34 6 22V10z"/><path d="M15 24l7 7 12-13"/></svg>
    <h3>Intelligence And<br>Security</h3>
    <p>Lorem ipsum dolor sit amet, consectetuer adipiscing elit, sed diam nonummy nibh euismod tincidunt ut laoreet dolore magna</p>
    <span class="btn btn-sm">Read More</span>
  </article>
  <article class="service">
    <svg viewBox="0 0 48 48" fill="none" stroke="#0d4f9c" stroke-width="2.5"><rect x="4" y="30" width="10" height="10"/><rect x="19" y="30" width="10" height="10"/><rect x="19" y="16" width="10" height="10"/><rect x="34" y="16" width="10" height="10"/><rect x="34" y="3" width="10" height="10"/><rect x="4" y="16" width="10" height="10"/></svg>
    <h3>Automation<br>Systems</h3>
    <p>Lorem ipsum dolor sit amet, consectetuer adipiscing elit, sed diam nonummy nibh euismod tincidunt ut laoreet dolore magna</p>
    <span class="btn btn-sm">Read More</span>
  </article>
  <article class="service">
    <svg viewBox="0 0 48 48" fill="none" stroke="#0d4f9c" stroke-width="2.5"><path d="M12 38a9 9 0 0 1 0-18 13 13 0 0 1 25 2 8 8 0 0 1-1 16z"/><circle cx="18" cy="30" r="2.5"/><circle cx="30" cy="24" r="2.5"/><circle cx="30" cy="34" r="2.5"/><path d="M20 29l8-4M20 31l8 2"/></svg>
    <h3>Cloud<br>Solutions</h3>
    <p>Lorem ipsum dolor sit amet, consectetuer adipiscing elit, sed diam nonummy nibh euismod tincidunt ut laoreet dolore magna</p>
    <span class="btn btn-sm">Read More</span>
  </article>
</section>

<section class="mission abs">
  <h2>Our Mission</h2>
  <p>Lorem ipsum dolor sit amet, consectetuer adipiscing elit, sed diam nonummy nibh euismod tincidunt ut laoreet dolore magna aliquam erat volutpat. Ut wisi enim ad minim veniam, quis nostrud exerci tation ullamcorper suscipit lobortis nisl ut aliquip.</p>
  <span class="btn">Learn More</span>
</section>
<div class="mission-photo abs" role="img" aria-label="Smiling man in glasses holding an open laptop showing the company name"></div>

<div class="hiring-band abs"></div>
<div class="hiring-photo abs" role="img" aria-label="Group of five business people standing with arms crossed"></div>
<section class="hiring abs">
  <h2>We Are Hiring</h2>
  <p>Lorem ipsum dolor sit amet, consectetuer adipiscing elit, sed diam nonummy nibh euismod tincidunt ut laoreet dolore magna aliquam erat volutpat. Ut wisi enim ad minim veniam, quis nostrud exerci tation ullamcorper suscipit lobortis nisl ut aliquip.</p>
  <span class="btn">Apply Now</span>
</section>

<div class="partners abs" aria-label="Partner badges">
  <span class="partner round"></span><span class="partner"></span><span class="partner"></span><span class="partner"></span><span class="partner round"></span>
</div>
<div class="partners-rule abs"></div>

<footer class="footer abs">
  <div class="fcol about">
    <h4>About Us</h4>
    Lorem ipsum ex vix illud nonummy, novum tation et his. At vix scriptaset patrioque scribentur, at pro fugit eis veterem molestie, sed et vivendo all Lorem ipsum ex vix illud nonummy, novum tation et his. At vix scripta patrioque scribentur, sed et vivendo all Lorem ipsum ex vix illud nonummy, novum tation et his. At vix scripta patrioque scribentur...
  </div>
  <div class="fcol posts">
    <h4>Recent Posts</h4>
    <ul>
      <li>Voluptas Sadips Ipsums Dolors Untra</li>
      <li>Fugiats Litora Ultrices Ante Auctor</li>
      <li>Sapien Litora Dolores Ultrices</li>
      <li>Nemis Fugiats Voluptas Dolores Uns</li>
      <li>Fugiats Litora Ultrices Ante Auctor</li>
    </ul>
  </div>
  <div class="fcol tweets">
    <h4>Updates</h4>
    <p><b>@nolvane</b> <i>( What an awesome theme! We love it, tons of options and great design, thank you! )</i> 12 minutes ago</p>
    <p><b>@nolvane</b> <i>you've got to check this one out, very cool looking!</i> 25 minutes ago</p>
    <p><b>@nolvane</b> <i>( What an awesome theme! We love it, tons of options and great design, thank you! )</i> 12 minutes ago</p>
  </div>
  <div class="fcol contact">
    <h4>Contact Us</h4>
    410 Harrow Point Drive,<br>Suite 120 East<br>Cedar Falls, CO 80512
    <div class="row"><svg width="12" height="12" viewBox="0 0 24 24"><path fill="#a9adb2" d="M6.6 10.8a15 15 0 0 0 6.6 6.6l2.2-2.2c.3-.3.7-.4 1-.2 1.1.4 2.3.6 3.6.6.6 0 1 .4 1 1V20c0 .6-.4 1-1 1A17 17 0 0 1 3 4c0-.6.4-1 1-1h3.5c.6 0 1 .4 1 1 0 1.3.2 2.5.6 3.6.1.3 0 .7-.2 1z"/></svg>(555) 214-0387</div>
    <div class="row"><svg width="12" height="10" viewBox="0 0 24 20"><rect width="24" height="20" rx="2" fill="#a9adb2"/><rect x="3" y="4" width="18" height="3" fill="#2e3034"/></svg>http://www.lumavex.com</div>
    <div class="row"><svg width="12" height="10" viewBox="0 0 26 20"><rect width="26" height="20" rx="2" fill="#a9adb2"/><path d="M2 3l11 8 11-8" stroke="#2e3034" stroke-width="2" fill="none"/></svg>info@lumavex.com</div>
  </div>
</footer>

<div class="bottom-bar abs">
  <span class="copy abs">copyright© 2014 LVM. All Rights Reserved</span>
  <span class="tip abs">Follow</span>
  <div class="social abs"><span></span><span></span><span></span><span></span><span></span></div>
</div>

</body>
</html>
```